DL flyer for mobile auto electrician

We need a DL flyer designed for distribution outlining the services provided by our mobile auto electrical business. Logo and text will be provided. The flyer will be distributed with the local newspaper and other advertising materials so we need something that will stand out from the crowd!

Our business is 'Brightpath Motor Electrics' and our colours are blue and red which you will be able to see through the logo.

Industry/Entity Type

Electrician

```html
<!DOCTYPE html>
<html lang="en">
<head>
<meta charset="utf-8">
<title>Brightpath Motor Electrics – DL Flyer</title>
<link rel="stylesheet" href="https://fonts.googleapis.com/css2?family=Saira+Condensed:wght@300;400;600;700&display=swap">
<style>
  :root {
    --bg: #8f8f8f;
    --paper: #ffffff;
    --brand-blue: #2f9bd6;
    --brand-red: #d8232e;
    --red-deep: #a9161f;
    --red-bright: #e4323b;
    --footer-blue: #34a3dc;
    --photo-dark: #2c3442;
    --photo-mid: #5b6878;
    --photo-light: #b9c2cc;
    --ink-white: #ffffff;
  }
  * { box-sizing: border-box; margin: 0; padding: 0; }
  html, body {
    width: 1158px; height: 1200px; overflow: hidden;
    background: linear-gradient(180deg, #9a9a9a 0%, var(--bg) 100%);
    font-family: "Saira Condensed", "Arial Narrow", sans-serif;
  }
  .flyer {
    position: absolute; left: 314px; top: 40px;
    width: 530px; height: 1120px;
    background: var(--paper);
    overflow: hidden;
    box-shadow: 0 8px 24px rgba(0,0,0,.25);
  }
  .header {
    position: absolute; left: 0; top: 0; width: 100%; height: 160px;
    display: flex; align-items: center; justify-content: center; gap: 14px;
  }
  .brand-mark {
    width: 20px; height: 20px; border-radius: 50%;
    background: var(--brand-red);
  }
  .brand-name {
    color: var(--brand-blue); font-weight: 600;
    font-size: 40px; line-height: 1; letter-spacing: .5px;
  }
  .hero-photo {
    position: absolute; left: 36px; top: 160px; width: 494px; height: 380px;
    background: linear-gradient(135deg, var(--photo-light) 0%, var(--photo-mid) 45%, var(--photo-dark) 100%);
    clip-path: polygon(0 0, 100% 0, 100% 74%, 0 100%);
  }
  .services {
    position: absolute; left: 36px; top: 0; width: 494px; height: 1120px;
    background: radial-gradient(ellipse at 60% 55%, var(--red-bright) 0%, var(--brand-red) 45%, var(--red-deep) 100%);
    clip-path: polygon(0 550px, 100% 460px, 100% 1040px, 0 1120px);
  }
  .services-content {
    position: absolute; left: 36px; top: 540px; width: 494px;
    text-align: center; color: var(--ink-white);
  }
  .headline {
    font-weight: 700; font-size: 29px; line-height: 1.05;
    padding: 0 30px;
  }
  .divider {
    width: 300px; height: 1.5px; background: var(--ink-white);
    margin: 22px auto 20px;
  }
  .service-list { list-style: none; font-weight: 300; font-size: 27px; line-height: 1.12; }
  .footer {
    position: absolute; left: 36px; top: 0; width: 494px; height: 1120px;
    background: var(--footer-blue);
    clip-path: polygon(0 1120px, 100% 1040px, 100% 1120px);
  }
  .contact {
    position: absolute; left: 36px; top: 1000px; width: 494px; height: 120px;
    display: flex; flex-direction: column; justify-content: flex-end;
    padding: 0 10px 16px; text-align: center;
    color: var(--ink-white); font-weight: 400; font-size: 14px; line-height: 1.35;
  }
  .contact-band {
    position: absolute; left: 36px; top: 1050px; width: 494px; height: 70px;
    background: var(--footer-blue);
  }
  .left-margin {
    position: absolute; left: 0; top: 160px; width: 36px; height: 960px;
    background: var(--paper);
  }
</style>
</head>
<body>
  <main class="flyer">
    <header class="header">
      <span class="brand-mark"></span>
      <span class="brand-name">Brightpath Motor Electrics</span>
    </header>

    <div class="hero-photo" role="img" aria-label="Photo of a mechanic in a blue cap testing a car engine's wiring with a multimeter under an open bonnet"></div>

    <section class="services" role="img" aria-label="Red-tinted photo of engine wiring behind the service list"></section>
    <div class="services-content">
      <h1 class="headline">Experienced mobile auto electrician servicing all residential, commercial and heavy duty vehicles.</h1>
      <div class="divider"></div>
      <ul class="service-list">
        <li>Spotlights and dual battery systems</li>
        <li>Air conditioning</li>
        <li>Camper trailers</li>
        <li>Boats</li>
        <li>Mine site fit outs</li>
        <li>All aspects of diagnosis and repairs</li>
      </ul>
    </div>

    <div class="contact-band"></div>
    <div class="contact">
      <p>Contact us: Reid Callahan &nbsp;|&nbsp; P: 0400 555 218 &nbsp;|&nbsp; E: rcallahan@mail.example</p>
      <p>ABN 51 824 307 166 &nbsp;|&nbsp; AU50218</p>
    </div>

    <div class="left-margin"></div>
  </main>
</body>
</html>
```